Design website for new email startup

We are starting a company called Posta.QZ (it will live at http://posta.qz.example).

We would like the main landing page for our site designed. We have provided a very simple wireframe to help provide direction for the content it should include, but we do not expect the designers to adhere to it at all - we encourage unique ideas. There is some sample text in the wireframe - this does not have to be used, but may provide ideas.

We provide an easy way for people to manage email for a custom domain name. For example if you own "myfamilyword.example" you can point your DNS records to us and we'll make it easy to have emails addressed to your domain get forwarded to your existing email (vexmail, etc). Folks running blogs, and other small sites can quickly setup email addresses for their domains and manage them in one place.

(For technical folks, we have you point your dns mx records to us, hence the name. That way all your email hits us and we can redirect it wherever you want. We make it easy to manage a single domain or a bunch of domains. Many domain registrars offer this service for a fee, and have clumsy management tools. We provide a robust simple toolset for free, as well as premium options).

The goal of the landing page is to get folks into the signup flow. The second priority flow is to have them take a look at the premium plan offerings.

We may offer the winning designer additional work for the remainder of the site design.
Updates

I've changed this project to a committed payment.  It is no longer refundable.  Thank you.

Target Market(s)

Bloggers, podcasters, designers, app developers - people who are a little tech savvy.

Industry/Entity Type

It Company

Font styles to use
Sans Serif

Colors

Designer to choose colors to be used in the design.

Requirements
Must have
• A full fidelity mockup (comp) of the landing page including the source file (psd, ai, etc).

Some sort of logo treatment for the posta.qz brand

A call to action for signup, such as the suggested 'Get Started Here'
Nice to have
• A hip startup feel

Incorporation of the email theme

Give the impression it is simple, easy and fast

```html
<!DOCTYPE html>
<html lang="en">
<head>
<meta charset="utf-8">
<title>Posta.QZ — We Make Email Easy</title>
<link href="https://fonts.googleapis.com/css2?family=Open+Sans:wght@300;400;600;700;800&display=swap" rel="stylesheet">
<style>
  :root {
    --header-bg: #efefed;
    --ink: #121212;
    --nav-text: #3a3a3a;
    --nav-blue: #3a93cf;
    --nav-orange: #f0a24a;
    --nav-coral: #ee8a68;
    --hero-top: #7e97a6;
    --hero-mid: #8a9aa3;
    --hero-edge: #6e8ea3;
    --white: #ffffff;
    --hero-text: #eef2f5;
    --cta-blue: #3a8fcc;
    --cta-blue-dark: #2c7ab5;
    --cta-dark: #3d3d3d;
    --cta-dark-deep: #2c2c2c;
    --or-text: #262626;
    --band-blue: #3d94ca;
    --divider: #2f7fb3;
    --footer-bg: #1b1b1b;
    --footer-text: #e8e8e8;
  }
  * { margin: 0; padding: 0; box-sizing: border-box; }
  html, body { width: 1200px; height: 850px; overflow: hidden; }
  body { font-family: "Open Sans", Arial, sans-serif; position: relative; background: var(--white); }

  .site-header { position: absolute; left: 0; top: 0; width: 1200px; height: 75px; background: var(--header-bg); }
  .brand { position: absolute; left: 202px; top: 14px; font-size: 35px; font-weight: 700; letter-spacing: -1px; color: var(--ink); line-height: 1; }
  .main-nav { position: absolute; left: 804px; top: 0; height: 75px; display: flex; gap: 3px; }
  .main-nav a { display: block; width: 64px; height: 75px; padding-top: 48px; text-align: center; font-size: 10.5px; line-height: 14px; white-space: nowrap; color: var(--nav-text); text-decoration: none; border-bottom: 5px solid; }
  .main-nav .nav-how { border-color: var(--nav-blue); letter-spacing: -0.5px; }
  .main-nav .nav-support { border-color: var(--nav-orange); }
  .main-nav .nav-login { border-color: var(--nav-coral); }

  .hero { position: absolute; left: 0; top: 75px; width: 1200px; height: 487px; text-align: center; overflow: hidden; }
  .hero-backdrop { position: absolute; inset: 0; background: radial-gradient(ellipse at 50% 45%, var(--hero-mid) 0%, var(--hero-top) 55%, var(--hero-edge) 100%); }
  .hero-title { position: relative; margin-top: 75px; font-size: 52px; font-weight: 700; letter-spacing: -2.5px; color: var(--white); line-height: 1.2; }
  .hero-lede { position: relative; margin-top: 1px; font-size: 16.5px; font-weight: 300; letter-spacing: -0.8px; color: var(--hero-text); line-height: 24px; }
  .cta { position: absolute; left: 502px; width: 235px; height: 40px; border-radius: 3px; font-size: 21px; font-weight: 700; color: var(--white); line-height: 40px; text-decoration: none; text-align: center; }
  .cta-start { top: 283px; background: linear-gradient(var(--cta-blue), var(--cta-blue-dark)); }
  .cta-plans { top: 369px; background: linear-gradient(var(--cta-dark), var(--cta-dark-deep)); letter-spacing: 0.5px; }
  .cta-or { position: absolute; left: 0; width: 1200px; top: 336px; font-size: 20px; font-weight: 700; color: var(--or-text); }

  .partner-band { position: absolute; left: 0; top: 562px; width: 1200px; height: 226px; background: var(--band-blue); }
  .partner-band::after { content: ""; position: absolute; left: 600px; top: 28px; width: 1px; height: 156px; background: var(--divider); }
  .partner { position: absolute; top: 16px; width: 320px; text-align: center; color: var(--white); }
  .partner-left { left: 239px; }
  .partner-right { left: 639px; }
  .partner-heading { font-size: 14.5px; font-weight: 700; line-height: 17px; letter-spacing: 0.2px; }
  .partner-mark { height: 104px; margin-top: 12px; display: flex; align-items: center; justify-content: center; gap: 10px; font-size: 30px; font-weight: 700; color: var(--ink); }
  .partner-mark .dot { width: 26px; height: 26px; border-radius: 50%; background: var(--ink); }
  .read-more { display: block; margin-top: 28px; font-size: 11.5px; color: var(--white); text-decoration: none; }

  .band-rule { position: absolute; left: 0; top: 788px; width: 1200px; height: 3px; background: var(--white); }
  .site-footer { position: absolute; left: 0; top: 791px; width: 1200px; height: 59px; background: var(--footer-bg); color: var(--footer-text); font-size: 12px; text-align: center; line-height: 56px; }
</style>
</head>
<body>
  <header class="site-header">
    <div class="brand">Posta.QZ</div>
    <nav class="main-nav">
      <a class="nav-how" href="#">How It Works</a>
      <a class="nav-support" href="#">Support</a>
      <a class="nav-login" href="#">Login</a>
    </nav>
  </header>

  <section class="hero">
    <div class="hero-backdrop" role="img" aria-label="Soft blue-grey network pattern of linked circles"></div>
    <h1 class="hero-title">WE MAKE EMAIL EASY</h1>
    <p class="hero-lede">Give Us Five Minutes And We’ll Get You Email Form Your Domain<br>Easily Forward Mail Form Your Custom Domain Name Wherever&nbsp; You Want It<br>You Take The Mail, We’ll Keep The Spam</p>
    <a class="cta cta-start" href="#">GET STARTED HERE</a>
    <div class="cta-or">OR</div>
    <a class="cta cta-plans" href="#">COMPARE PLANS</a>
  </section>

  <section class="partner-band">
    <div class="partner partner-left">
      <h2 class="partner-heading">How to configure your SkyRelay DNS to use POSTA.QZ</h2>
      <div class="partner-mark"><span class="dot"></span>SkyRelay</div>
      <a class="read-more" href="#">READMORE</a>
    </div>
    <div class="partner partner-right">
      <h2 class="partner-heading">Use posta with your DomainPal domain registration for reliable email forwarding</h2>
      <div class="partner-mark"><span class="dot"></span>DomainPal</div>
      <a class="read-more" href="#">READMORE</a>
    </div>
  </section>
  <div class="band-rule"></div>

  <footer class="site-footer">Copyright 2014&nbsp; Posta.QZ | All Rights Reserved | Powered by Posta.QZ</footer>
</body>
</html>
```